Cosmetics Brand Logo and Bottle Label Design

We are creating a new cosmetics brand called "Nolan Whitby" and would like you to create an amazing logo and bottle label for this brand's new 100% pure argan oil product.
For the logo, we really like the logo's of Marin Calloway and Vessa. The text should be Sans Serif (without feet).
For the actual bottle label, please find attached labels of one of our competitors design which really like. We really like the simplicity and elegance of the design. The only difference is that our product will be using light turqoise as the brand color. Please feel free to add your own creativity into it as well.
Industry/Entity Type
Cosmetics
Logo Text
Nolan Whitby
Font styles to use

```html
<!DOCTYPE html>
<html lang="en">
<head>
<meta charset="utf-8">
<title>Nolan Whitby — Toner Labels</title>
<link rel="stylesheet" href="https://fonts.googleapis.com/css2?family=Montserrat:wght@300;400&family=Playfair+Display:ital,wght@0,400;1,400&display=swap">
<style>
  :root {
    --backdrop: #546660;
    --bottle: #463834;
    --label-light: #84cbbf;
    --label-deep: #27b4a2;
    --ink: #3a3431;
    --paper: #ffffff;
    --brand-tint: #7fcabd;
  }
  * { margin: 0; padding: 0; box-sizing: border-box; }
  html, body { width: 1200px; height: 848px; overflow: hidden; }
  body { background: var(--backdrop); position: relative; font-family: "Montserrat", sans-serif; }

  .bottle {
    position: absolute;
    width: 218px;
    background: var(--bottle);
    border-radius: 60px 60px 44px 44px;
  }
  .bottle--left { left: 230px; top: 62px; height: 630px; }
  .bottle--middle { left: 486px; top: 69px; height: 629px; }
  .bottle--right { left: 733px; top: 69px; height: 629px; }

  .label {
    position: absolute;
    width: 218px;
    background: var(--label-light);
    overflow: hidden;
    color: var(--paper);
  }
  .label::before {
    content: "";
    position: absolute;
    inset: 0;
    background: linear-gradient(160deg, var(--label-light) 15%, var(--label-deep) 100%);
    clip-path: polygon(42px 100%, 100% 64px, 100% 100%);
  }
  .label > * { position: absolute; z-index: 1; }
  .label--left { left: 230px; top: 334px; height: 303px; }
  .label--middle { left: 486px; top: 341px; height: 302px; }
  .label--right { left: 733px; top: 341px; height: 302px; }

  .brand-name {
    font-weight: 300;
    color: var(--ink);
    white-space: nowrap;
    text-transform: uppercase;
  }
  .label--left .brand-name {
    font-size: 19px;
    letter-spacing: 5px;
    left: 10px;
    bottom: 22px;
    transform-origin: left bottom;
    transform: translateX(24px) rotate(-90deg);
  }
  .label--middle .brand-name { font-size: 16px; letter-spacing: 4.6px; left: 16px; top: 248px; }
  .label--right .brand-name { font-size: 16px; letter-spacing: 4.6px; left: 14px; top: 33px; }

  .product-name { font-family: "Playfair Display", serif; font-weight: 400; line-height: 1; }
  .tagline { font-family: "Playfair Display", serif; font-style: italic; line-height: 1.45; white-space: nowrap; }
  .volume { font-size: 12px; font-weight: 400; transform: translateX(-50%); }
  .rule { height: 1px; background: var(--paper); }

  .label--left .product-name { font-size: 24px; left: 67px; top: 175px; }
  .label--left .rule { left: 67px; top: 206px; width: 127px; }
  .label--left .tagline { font-size: 14px; left: 67px; top: 214px; }
  .label--left .volume { left: 122px; top: 264px; }

  .label--middle .product-name { font-size: 32px; left: 21px; top: 40px; }
  .label--middle .tagline { font-size: 16px; left: 26px; top: 82px; line-height: 1.55; }

  .label--right .product-name { font-size: 26px; left: 25px; top: 150px; }
  .label--right .rule { left: 25px; top: 189px; width: 165px; }
  .label--right .tagline { font-size: 16px; left: 25px; top: 198px; line-height: 1.55; }
  .label--right .volume { left: 114px; top: 258px; }

  .wordmark {
    position: absolute;
    left: 0; right: 0;
    top: 742px;
    text-align: center;
    font-weight: 300;
    font-size: 58px;
    letter-spacing: 14px;
    padding-left: 14px;
    color: var(--brand-tint);
    text-transform: uppercase;
  }
</style>
</head>
<body>
  <div class="bottle bottle--left" role="img" aria-label="Dark amber dropper bottle"></div>
  <div class="bottle bottle--middle" role="img" aria-label="Dark amber dropper bottle"></div>
  <div class="bottle bottle--right" role="img" aria-label="Dark amber dropper bottle"></div>

  <section class="label label--left">
    <p class="brand-name">Nolan Whitby</p>
    <h2 class="product-name">Toner</h2>
    <div class="rule"></div>
    <p class="tagline">tones and<br>conditions skin</p>
    <p class="volume">120 ml</p>
  </section>

  <section class="label label--middle">
    <h2 class="product-name">Toner</h2>
    <p class="tagline">tones and<br>conditions skin</p>
    <p class="brand-name">Nolan Whitby</p>
  </section>

  <section class="label label--right">
    <p class="brand-name">Nolan Whitby</p>
    <h2 class="product-name">Toner</h2>
    <div class="rule"></div>
    <p class="tagline">tones and<br>conditions skin</p>
    <p class="volume">120 ml</p>
  </section>

  <h1 class="wordmark">Nolan Whitby</h1>
</body>
</html>
```